Cybersecurity company is looking for business card.

I need a business card design for our company, we are a cybersecurity company providing advance technology to protect agains any kind of malware. We need a fresh modern design it should communicate modern, technology and growth.

Target Market(s)

Business to business

Industry/Entity Type

Business

Contact Information for Business Card

Should have location, address, fax, mobile, phone, email and website.

Requirements
Must have
• Must follow company's logo color and style. Must have the company's log on its.

```html
<!DOCTYPE html>
<html lang="en">
<head>
<meta charset="utf-8">
<title>Vextora Business Card</title>
<link href="https://fonts.googleapis.com/css2?family=Roboto:wght@400;700&display=swap" rel="stylesheet">
<style>
  :root {
    --page-bg: #e6e4e0;
    --card-yellow: #ecec12;
    --card-yellow-light: #f4f43a;
    --card-white: #ffffff;
    --ink: #2b2b2b;
    --ink-soft: #3a3a3a;
  }
  * { margin: 0; padding: 0; box-sizing: border-box; }
  html, body {
    width: 1200px;
    height: 1024px;
    overflow: hidden;
    background: var(--page-bg);
    font-family: "Roboto", Arial, sans-serif;
  }
  .card {
    position: absolute;
    left: 280px;
    width: 640px;
    height: 366px;
    border-radius: 4px;
    box-shadow: 0 6px 18px rgba(0,0,0,0.18);
  }
  .card-front {
    top: 110px;
    background: linear-gradient(160deg, var(--card-yellow-light) 0%, var(--card-yellow) 60%);
  }
  .card-back {
    top: 548px;
    background: var(--card-white);
  }
  .brand-name {
    position: absolute;
    right: 60px;
    top: 58px;
    font-size: 112px;
    font-weight: 700;
    letter-spacing: -2px;
    color: var(--ink);
    line-height: 1;
  }
  .contact-list {
    position: absolute;
    left: 34px;
    bottom: 30px;
    list-style: none;
  }
  .contact-item {
    display: flex;
    align-items: center;
    gap: 8px;
    font-size: 14px;
    line-height: 19px;
    color: var(--ink-soft);
    white-space: nowrap;
  }
  .contact-icon {
    width: 11px;
    height: 11px;
    flex: none;
    fill: var(--ink-soft);
  }
</style>
</head>
<body>
  <section class="card card-front" aria-label="Business card front">
    <div class="brand-name">vextora</div>
    <ul class="contact-list">
      <li class="contact-item">
        <svg class="contact-icon" viewBox="0 0 12 12"><path d="M6 0a4 4 0 0 0-4 4c0 3 4 8 4 8s4-5 4-8a4 4 0 0 0-4-4zm0 5.6A1.6 1.6 0 1 1 6 2.4a1.6 1.6 0 0 1 0 3.2z"/></svg>
        Northport - Coastland
      </li>
      <li class="contact-item">
        <svg class="contact-icon" viewBox="0 0 12 12"><path d="M6 1 0 6h2v5h3V8h2v3h3V6h2z"/></svg>
        Harbor Tech Park (HTP) - Meridian Avenue
      </li>
      <li class="contact-item">
        <svg class="contact-icon" viewBox="0 0 12 12"><path d="M3.5 0h5a1 1 0 0 1 1 1v10a1 1 0 0 1-1 1h-5a1 1 0 0 1-1-1V1a1 1 0 0 1 1-1zm.5 1.5v7.5h4V1.5zM6 9.8a.7.7 0 1 0 0 1.4.7.7 0 0 0 0-1.4z"/></svg>
        +44 71 486 2290
      </li>
      <li class="contact-item">
        <svg class="contact-icon" viewBox="0 0 12 12"><path d="M2.5 0.5 4.5 3 3.3 4.4a7 7 0 0 0 4.3 4.3L9 7.5l2.5 2L10.3 11.5C5 11.5.5 7 .5 1.7z"/></svg>
        02 362 5817
      </li>
      <li class="contact-item">
        <svg class="contact-icon" viewBox="0 0 12 12"><path d="M3 0h5v3H3zM1 4h10v5H9v3H3V9H1zm3 5v2h4V9z"/></svg>
        02 362 5818
      </li>
      <li class="contact-item">
        <svg class="contact-icon" viewBox="0 0 12 12"><path d="M0 2h12v8H0zm1 1v.4l5 3.2 5-3.2V3zm0 1.6V9h10V4.6L6 7.8z"/></svg>
        name.surname@vextora.com
      </li>
      <li class="contact-item">
        <svg class="contact-icon" viewBox="0 0 12 12"><path d="M6 0a6 6 0 1 0 0 12A6 6 0 0 0 6 0zm0 1.2c.7.6 1.3 1.9 1.5 3.8h-3C4.700 3.1 5.3 1.8 6 1.2zM1.3 5h2.2c.1-1.4.4-2.6.9-3.4A4.8 4.8 0 0 0 1.3 5zm7.2 0h2.2a4.8 4.8 0 0 0-3.1-3.4c.5.8.8 2 .9 3.4zM1.3 7a4.8 4.8 0 0 0 3.1 3.4c-.5-.8-.8-2-.9-3.4zm3.2 0c.2 1.9.8 3.2 1.5 3.8.7-.6 1.3-1.9 1.5-3.8zm4 0c-.1 1.4-.4 2.6-.9 3.4A4.8 4.8 0 0 0 10.7 7z"/></svg>
        www.vextora.com
      </li>
    </ul>
  </section>
  <section class="card card-back" aria-label="Business card back"></section>
</body>
</html>
```